Gourmet cookie company needs a label designed

We need a label designed for a new cookie company. We make mini cookies. The labels will be placed on either white tins or clear containers. We would like some bright and eye catching label although not child like. Our target customer is adults not kids.
Any color/colors acceptable. The initial label will be a square 4" label but the design should also be able to be formatted to fit on a round label as well in the future.

Text on label: Rosalind's Wafer Crumb Company; Chocolate Chip; All Natural; New Wt. 8.0oz

```html
<!DOCTYPE html>
<html lang="en">
<head>
<meta charset="utf-8">
<title>Rosalind's Wafer Crumb Company – Chocolate Chip Label</title>
<link rel="stylesheet" href="https://fonts.googleapis.com/css2?family=Fira+Sans+Condensed:wght@600&family=Questrial&display=swap">
<style>
  :root {
    --gold: #dcae0e;
    --gold-soft: #e9c85c;
    --ink: #2a1d12;
    --paper: #ffffff;
    --edge: #9a9a9a;
  }
  * { margin: 0; padding: 0; box-sizing: border-box; }
  html, body { width: 1200px; height: 900px; overflow: hidden; background: var(--paper); }
  .canvas {
    position: relative;
    width: 1200px; height: 900px;
    border: 1px solid var(--edge);
    background: var(--paper);
  }
  .label {
    position: absolute;
    left: 226px; top: 76px;
    width: 748px; height: 748px;
    border: 1px solid #6f6f6f;
    background: var(--paper);
  }
  .label-frame {
    position: absolute;
    left: 24px; top: 24px;
    width: 698px; height: 699px;
    border: 4px solid var(--gold);
    overflow: hidden;
  }
  .brand-name {
    position: absolute;
    left: 0; right: 0; top: 150px;
    text-align: center;
    font-family: "Fira Sans Condensed", sans-serif;
    font-weight: 600;
    font-size: 46px;
    color: var(--gold);
    letter-spacing: 0.5px;
  }
  .flavor-band {
    position: absolute;
    left: 10px; right: 10px; top: 346px;
    height: 90px;
    background: linear-gradient(90deg, rgba(233,200,92,0) 0%, var(--gold-soft) 12%, var(--gold-soft) 88%, rgba(233,200,92,0) 100%);
    display: flex; align-items: center; justify-content: center;
  }
  .flavor-name {
    font-family: "Fira Sans Condensed", sans-serif;
    font-weight: 600;
    font-size: 48px;
    color: var(--ink);
    letter-spacing: 0.5px;
  }
  .lower-panel {
    position: absolute;
    left: 0; right: 0; top: 436px; bottom: 0;
    background: linear-gradient(180deg, var(--paper) 0%, #f7eac0 30%, #ecd27a 70%, var(--gold) 100%);
  }
  .claim, .net-weight {
    position: absolute;
    left: 0; right: 0;
    text-align: center;
    font-family: "Questrial", sans-serif;
    color: var(--ink);
  }
  .claim { top: 86px; font-size: 32px; }
  .net-weight { top: 212px; font-size: 29px; }
</style>
</head>
<body>
  <div class="canvas">
    <div class="label">
      <div class="label-frame">
        <div class="brand-name">Rosalind's Wafer Crumb Company</div>
        <div class="flavor-band"><span class="flavor-name">CHOCOLATE CHIP</span></div>
        <div class="lower-panel">
          <p class="claim">All Natural</p>
          <p class="net-weight">New Wt. 8.0oz</p>
        </div>
      </div>
    </div>
  </div>
</body>
</html>
```